New Packaging Design for Hair Extensions!

We're an Australian based hair extensions company looking for a fresh new design for our hair extensions packaging.
We have recently re-designed our website and now need our packaging to match the new premium feel. You can check out our website at www.brevinatresses.com.au
Our current packaging is like most hair extension packaging out there - a cardboard insert inside a clear plastic bag. We don't feel this packaging reflects the quality and price of our product (around the $150-$200 mark) and want customers to feel a sense of quality when they receive their order.
We would like to change our packaging to a box design (we've attached a few example photos we've found online) or something similar.
In regards to design, less is more - we want something that looks high end, but still has a hint of fun. (our target market is women ages 19-30)
Colours to be used: Black, white, pink, dark grey (as per our website)
Women 19-30
Hair

```html
<!DOCTYPE html>
<html lang="en">
<head>
<meta charset="utf-8">
<title>Brevina Hair Extensions – Packaging</title>
<link rel="stylesheet" href="https://fonts.googleapis.com/css2?family=Montserrat:wght@500;700&family=Oswald:wght@400;500;600&display=swap">
<style>
  :root{
    --bg:#c4c4c4;
    --white:#ffffff;
    --pink:#d1358f;
    --pink-deep:#b81f79;
    --plum:#5a1140;
    --grey-light:#e4e4e4;
    --grey-mid:#cfcfcf;
    --grey-dark:#3a3a3a;
    --hair-dark:#4a2f1c;
    --hair-mid:#7a5232;
    --hair-light:#a57a50;
  }
  *{box-sizing:border-box;margin:0;padding:0}
  html,body{width:1200px;height:1000px;overflow:hidden;background:var(--bg)}
  .canvas{position:relative;width:1200px;height:1000px}

  /* inner lid panel */
  .lid-panel{
    position:absolute;left:40px;top:380px;width:760px;height:240px;
    background:linear-gradient(180deg,var(--grey-light),var(--grey-mid));
    overflow:hidden;
  }
  .lid-panel__portrait{
    position:absolute;left:0;top:0;width:240px;height:100%;
    background:linear-gradient(135deg,#bdbdbd,#8f8f8f 55%,#d6d6d6);
  }
  .lid-panel__heart{position:absolute;left:250px;top:40px;width:170px;height:160px}
  .lid-panel__text{
    position:absolute;left:255px;top:96px;width:360px;
    text-align:center;white-space:nowrap;
  }
  .lid-panel__care{
    font-family:'Oswald',sans-serif;font-weight:500;font-size:16px;
    letter-spacing:.3px;color:var(--grey-dark);line-height:1.4;
  }
  .lid-panel__visit{
    font-family:'Oswald',sans-serif;font-weight:400;font-size:15px;
    letter-spacing:.6px;color:#555;line-height:1.5;
  }
  .lid-panel__seal{
    position:absolute;right:20px;top:65px;width:110px;height:110px;border-radius:50%;
    background:var(--pink);display:flex;align-items:center;justify-content:center;
    font-family:'Montserrat',sans-serif;font-weight:700;font-size:23px;color:var(--white);
  }

  /* front sleeve */
  .front-panel{
    position:absolute;left:850px;top:40px;width:310px;height:920px;
    background:var(--white);
  }
  .badge{
    position:absolute;left:95px;top:18px;width:120px;height:120px;border-radius:50%;
    background:var(--pink);border:4px solid #e58cbd;
    display:flex;flex-direction:column;align-items:center;
    font-family:'Oswald',sans-serif;color:var(--white);
  }
  .badge__count{font-size:34px;font-weight:600;line-height:1;margin-top:12px}
  .badge__unit{font-size:18px;font-weight:500;line-height:1.1}
  .badge__label{font-size:11px;letter-spacing:1px;margin-top:2px}
  .badge__colour{
    background:var(--white);color:var(--grey-dark);font-size:11px;
    padding:0 16px;margin-top:2px;letter-spacing:1px;
  }
  .brand{
    position:absolute;left:0;top:150px;width:100%;text-align:center;
    font-family:'Montserrat',sans-serif;font-weight:700;font-size:50px;
    color:var(--pink);line-height:1;
  }
  .brand__sub{
    position:absolute;left:30px;right:30px;top:210px;text-align:center;
    font-family:'Montserrat',sans-serif;font-weight:500;font-size:19px;
    color:var(--plum);letter-spacing:1px;padding-bottom:4px;
    border-bottom:2px solid var(--pink);
  }
  .window{position:absolute;left:18px;top:262px;width:274px;height:450px}
  .window__hair{
    position:absolute;inset:0;
    background:linear-gradient(100deg,var(--hair-dark),var(--hair-mid) 35%,var(--hair-light) 55%,var(--hair-mid) 75%,var(--hair-dark));
    border-radius:26px 26px 0 0;
  }
  .window__arch{position:absolute;left:0;bottom:-1px;width:274px;height:60px}
  .love-mark{position:absolute;left:105px;top:718px;width:100px;height:34px}
  .tag{
    position:absolute;left:8px;top:764px;display:flex;
    font-family:'Oswald',sans-serif;font-weight:600;font-size:18px;color:var(--white);
  }
  .tag__pct{background:var(--plum);padding:1px 6px}
  .tag__text{background:var(--pink);padding:1px 10px;letter-spacing:.8px}
  .claim{
    position:absolute;left:8px;top:798px;white-space:nowrap;
    font-family:'Oswald',sans-serif;font-weight:600;font-size:30px;
    line-height:1.15;letter-spacing:.5px;
  }
  .claim__pink{color:var(--pink)}
  .claim__plum{color:var(--plum)}
</style>
</head>
<body>
<main class="canvas">

  <section class="lid-panel">
    <div class="lid-panel__portrait" role="img" aria-label="Black and white portrait of a woman with long wavy hair"></div>
    <svg class="lid-panel__heart" viewBox="0 0 100 95" aria-hidden="true">
      <path d="M50 92 C20 68 2 50 2 28 C2 12 14 2 28 2 C38 2 46 8 50 16 C54 8 62 2 72 2 C86 2 98 12 98 28 C98 50 80 68 50 92Z" fill="#ffffff" opacity=".45"/>
    </svg>
    <div class="lid-panel__text">
      <p class="lid-panel__care">• For Care Guide - How To Care For Hair Extensions •</p>
      <p class="lid-panel__visit">visit www.brevinatresses.com.au</p>
    </div>
    <div class="lid-panel__seal">brevina</div>
  </section>

  <section class="front-panel">
    <div class="badge">
      <span class="badge__count">2</span>
      <span class="badge__unit">PC.</span>
      <span class="badge__label">-COLOR:-</span>
      <span class="badge__colour">LOREM</span>
    </div>

    <h1 class="brand">brevina</h1>
    <p class="brand__sub">HAIR EXTENSIONS</p>

    <div class="window">
      <div class="window__hair" role="img" aria-label="Straight brunette hair extensions visible through the window"></div>
      <svg class="window__arch" viewBox="0 0 274 60" preserveAspectRatio="none" aria-hidden="true">
        <path d="M0 60 L0 30 Q137 -10 274 30 L274 60 Z" fill="#ffffff"/>
      </svg>
    </div>

    <svg class="love-mark" viewBox="0 0 100 34" aria-hidden="true">
      <circle cx="18" cy="20" r="4" fill="#5a1140"/>
      <path d="M50 32 C38 23 32 18 32 11 C32 6 36 2 41 2 C45 2 48 4 50 7 C52 4 55 2 59 2 C64 2 68 6 68 11 C68 18 62 23 50 32Z" fill="#d1358f"/>
      <circle cx="82" cy="20" r="4" fill="#5a1140"/>
    </svg>

    <div class="tag">
      <span class="tag__pct">100%</span>
      <span class="tag__text">REMY HUMAN HAIR</span>
    </div>

    <p class="claim">
      <span class="claim__pink">INSTANT</span> <span class="claim__plum">VOLUME</span><br>
      <span class="claim__pink">SHOW</span> <span class="claim__plum">STOPPING</span> <span class="claim__pink">HAIR.</span>
    </p>
  </section>

</main>
</body>
</html>
```